Acrylschild für Eingang
Zielgruppe
Projekt Acrylschild für Eingang
Wir sind ein Einzelhandel und Online-Shop im Bereich Wohnaccessoires und Mode im nordischen Stil. Unsere Zielgruppe sind eher Frauen von 20 bis 60 Jahren, trendbewußt und fit im Bereich Social Medias.
Aufgabenstellung
Grundsätzlich ist unser Motto: clean, nordisch, minimalistisch
Das Design sollte daher nur die wichtigsten Informationen enthalten und sich von der Optik bzw. den Schriftzügen an unseren Online-Shops orientieren. Auf jeden Fall nicht verspielt.
Das Projekt betrifft das Design eines Firmen Acrylschilds mit den Maßen 22 cm x 22 cm, dabei sollte beachtet werden, dass an den vier Ecken Befestigungen aus Edelstahl ihren Platz finden müssen.
Das Schild wird außen am Eingang auf Augenhöhe befestigt.
Darauf sollten folgende Informationen Platz finden:
- Logo
- der Text: nordic living
- Öffnungszeiten: Montag bis Samstag 10 bis 17 Uhr
- Telefonnummer: 07418 5126047
- Adresse Online-Shop: www.4heimform.de
...und eventuell als Möglichkeit ein QR-Code des Online-Shops
Das Logo und der Text nordic living (der auch klein geschrieben sein kann, eventuell auch kalligrafisch aber ohne Schnörkel z. B. ähnlich Schrift MINA) sollte 1 Bereich einnehmen
und etwas getrennt von den weiteren Informationen dargestellt werden.
Das Schild sollte nicht bunt oder farbige Hintergründe haben (die Wand dahinter ist in einem gebrochenen Weißton mit leicht rauher Struktur).

```html
<!DOCTYPE html>
<html lang="de">
<head>
<meta charset="utf-8">
<title>Kestrelund – Acrylschild Eingang</title>
<link href="https://fonts.googleapis.com/css2?family=Josefin+Sans:wght@300;400&display=swap" rel="stylesheet">
<style>
  :root {
    --backdrop: #f3f3f3;
    --sign: #ffffff;
    --ink: #1c1c1c;
    --ink-soft: #2e2e2e;
    --accent: #cfcac4;
    --shadow: rgba(0, 0, 0, 0.12);
  }
  * { margin: 0; padding: 0; box-sizing: border-box; }
  html, body {
    width: 1200px;
    height: 2400px;
    overflow: hidden;
    background: var(--backdrop);
  }
  .canvas {
    position: relative;
    width: 1200px;
    height: 2400px;
  }
  .sign {
    position: absolute;
    left: 50px;
    top: 650px;
    width: 1100px;
    height: 1100px;
    background: var(--sign);
    box-shadow: 0 10px 40px var(--shadow);
    font-family: "Josefin Sans", sans-serif;
    color: var(--ink);
    text-align: center;
  }
  .brand {
    position: absolute;
    top: 360px;
    left: 0;
    width: 100%;
    display: flex;
    justify-content: center;
    align-items: center;
    gap: 30px;
  }
  .brand-mark {
    width: 64px;
    height: 64px;
    border-radius: 50%;
    background: var(--accent);
  }
  .brand-name {
    font-size: 112px;
    font-weight: 400;
    letter-spacing: 0.04em;
    line-height: 1;
    padding-top: 14px;
  }
  .tagline {
    position: absolute;
    top: 615px;
    left: 0;
    width: 100%;
    font-size: 76px;
    font-weight: 300;
    letter-spacing: 0.24em;
    padding-left: 0.24em;
    line-height: 1;
  }
  .info {
    position: absolute;
    top: 835px;
    left: 0;
    width: 100%;
    list-style: none;
    font-size: 29px;
    font-weight: 400;
    letter-spacing: 0.12em;
    color: var(--ink-soft);
  }
  .info li { line-height: 54px; }
</style>
</head>
<body>
<div class="canvas">
  <section class="sign">
    <div class="brand">
      <span class="brand-mark"></span>
      <span class="brand-name">KESTRELUND</span>
    </div>
    <p class="tagline">NORDIC LIVING</p>
    <ul class="info">
      <li>ÖFFNUNGSZEITEN: MO.–SA. 10:00–17:00 UHR</li>
      <li>TELEFONNUMMER: 07418 5126047</li>
      <li>ONLINE-SHOP: WWW.4HEIMFORM.DE</li>
    </ul>
  </section>
</div>
</body>
</html>
```